Web Design Project

Parallel Press owns and operates a large number of editorial websites. These websites provides mostly consumers in the financial services space with information and price comparisons for a particular service.

Parallel Press, as the holding company for each of these sites, currently has no website. We need to build a website targeted towards potential partners for our websites. The idea being that when we start a conversation with a partner, they can view our site and obtain some basic information about who we are.

The structure of the site is to be very simple, containing only a brief description about who we are, our contact details and a list of some of our websites:
• LifeCoverHub.net.au
• MotorCoverCheckers.com.au
• HouseCoverCheckers.com.au
• MedicalCoverCheckers.com.au
• LivingCoverCheckers.com.au
• TripCoverCheckers.com.au
• AnimalCoverCheckers.com.au
• PrivateCreditCheckers.com.au
• MobileCoolingUnit.com.au
• FixedSavingYield.com.au
• ThriftyDays.com.au
• CashNana.com.au
• TameThePlastic.com.au
• PurseKeeper.com.au
• ThirdPartyClaimsCoverOz.com.au
• Trade-Protection.com.au
• MotorCoverProviders.com.au
• MedicalCoverProviders.com.au
• HouseCoverDownUnder.com
• LivingCoverDownUnder.com
• SalaryShieldCoverDownUnder.com
• MedicalCoverDownUnder.com
• AnimalCoverDownUnder.com
• PrivateCreditDownUnder.com
• PlasticPaysDownUnder.com
• HouseFinanceDownUnder.com
• RetireFundHub.net.au

The design of the site should say 'Internet company', 'professional', 'fresh thinking'. The design should not look like a corporate site that you would see from any corporate services business with images of people in suits. We are ultimately an Internet business and there should be a unique feel to the site.

We are open to a suggestion of a colour pallet as the holding company does not have an established logo.

Some sites that we like are:

http://www.brindle-studio.example/#home
http://preview11.layoutvault.example/wt_48261/index.html
http://preview11.layoutvault.example/wordpress_59134/
http://mulloptic.example/
http://www.tandrel.example/
http://www.kovasilindqvist.example/
http://www.sharpsitegallery.example/Corporate/design-ideas-detail.html?id=4172
http://brackenway.example/
http://oskarteel.example/

Reason: Hi all, Apologies, but I need to extend the timeline. One of our key stakeholders is away for the next week. There are a few good designs that we have received to date and there are some tweaks that we would like to see before making a final decision. Thank you to everyone that has submitted designs - Have a great new year. Bram

Reason: Sorry to have to delay the deadline on this, but we did not find anything in the designs really resonated with us. We will have a further think about the existing designs that have been submitted and how we can provide more specific feedback to the designers to make some modifications to the designs.

Target Market(s)

We are targeting insurance companies / brokers that we are talking to. The idea is that we show a professional face to them.

Industry/Entity Type

Financial

Requirements
Must have
• Home Page (possibly integrated with About us details)
Contact Us
Our Sites

```html
<!DOCTYPE html>
<html lang="en">
<head>
<meta charset="utf-8">
<title>Parallel Press</title>
<link rel="stylesheet" href="https://fonts.googleapis.com/css2?family=Arimo:wght@400;700&display=swap">
<style>
  :root {
    --sidebar: #616161;
    --sidebar-ink: #c4d8dc;
    --panel: #c4d8dc;
    --aside: #efefef;
    --page: #ffffff;
    --ink: #2b2b2b;
    --ink-soft: #3a3a3a;
    --muted: #8a8a8a;
    --pill: #efefef;
    --teal-light: #6cbac6;
    --teal-dark: #2c7a84;
    --grey-light: #a9a9a9;
    --grey-dark: #6e6e6e;
    --charcoal-light: #6a6666;
    --charcoal-dark: #2f2c2c;
    --rule: #8c9a9d;
  }
  * { box-sizing: border-box; margin: 0; padding: 0; }
  html, body { width: 1200px; height: 890px; overflow: hidden; background: var(--page); }
  body { font-family: "Arimo", Arial, sans-serif; color: var(--ink); position: relative; }

  .site { position: relative; width: 1200px; height: 890px; overflow: hidden; }

  /* right column */
  .aside {
    position: absolute; left: 700px; top: 0; width: 486px; height: 890px;
    background: var(--aside);
    box-shadow: 3px 0 6px rgba(0,0,0,0.12);
  }
  .aside-halo {
    position: absolute; left: 806px; top: -72px; width: 324px; height: 324px;
    border-radius: 50%; background: var(--panel);
  }
  .currency-badge {
    position: absolute; left: 878px; top: 38px; width: 180px; height: 180px; border-radius: 50%;
    background: radial-gradient(circle at 40% 30%, var(--teal-light) 0%, #4a9ca8 50%, var(--teal-dark) 100%);
    border: 3px solid #8cc6cf;
    box-shadow: 0 3px 6px rgba(0,0,0,0.25);
    display: flex; align-items: center; justify-content: center;
    color: #fff; font-weight: 700; font-size: 150px; line-height: 1;
    text-shadow: 3px 4px 4px rgba(0,0,0,0.35);
  }

  /* main panel */
  .main {
    position: absolute; left: 110px; top: 0; width: 608px; height: 890px;
    background: var(--panel);
  }
  .main-tab {
    position: absolute; left: 668px; top: 313px; width: 100px; height: 100px; border-radius: 50%;
    background: var(--panel);
    box-shadow: 3px 2px 5px rgba(0,0,0,0.18);
  }
  .main-tab-cover { position: absolute; left: 660px; top: 300px; width: 58px; height: 126px; background: var(--panel); }

  /* sidebar */
  .sidebar { position: absolute; left: 0; top: 0; width: 110px; height: 890px; background: var(--sidebar); }
  .sidebar-tab {
    position: absolute; left: 57px; top: 311px; width: 100px; height: 102px; border-radius: 50%;
    background: var(--sidebar);
    box-shadow: 3px 2px 5px rgba(0,0,0,0.22);
  }
  .sidebar-tab-cover { position: absolute; left: 0; top: 300px; width: 110px; height: 126px; background: var(--sidebar); }
  .brand-mark {
    position: absolute; left: 0; top: 54px; width: 110px; text-align: center;
    color: var(--sidebar-ink); font-weight: 700; font-size: 19px; line-height: 1.15;
  }
  .scroll-arrow { position: absolute; left: 33px; top: 196px; width: 48px; height: 56px; }
  .section-label {
    position: absolute; left: 57px; top: 355px; transform: translate(-50%, -50%) rotate(-90deg);
    color: var(--sidebar-ink); font-weight: 700; font-size: 27px; letter-spacing: 1px; white-space: nowrap;
  }

  /* title */
  .title-pill {
    position: absolute; left: 172px; top: 52px; width: 504px; height: 88px; border-radius: 44px;
    background: var(--pill);
    box-shadow: inset 0 4px 5px rgba(0,0,0,0.28);
    display: flex; align-items: center; justify-content: center;
  }
  .title-pill h1 { font-weight: 700; font-size: 46px; color: #111; letter-spacing: 0.5px; }

  .intro {
    position: absolute; left: 175px; top: 168px; width: 520px;
    font-size: 14.4px; line-height: 18.5px; letter-spacing: 0.45px; color: var(--ink-soft);
  }
  .divider { position: absolute; left: 172px; top: 474px; width: 520px; height: 1px; background: var(--rule); }

  .news { position: absolute; left: 180px; top: 522px; width: 516px; }
  .news h2 { font-size: 25px; font-weight: 700; color: var(--ink); margin-bottom: 12px; }
  .news-item time { display: block; font-size: 14px; font-weight: 700; color: var(--ink); letter-spacing: 0.4px; }
  .news-item h3 { font-size: 11.5px; font-weight: 700; letter-spacing: 0.6px; color: var(--ink); margin: 8px 0 6px; }
  .news-item p { font-size: 11.6px; line-height: 14px; letter-spacing: 0.5px; color: var(--ink-soft); }
  .news-item.second { margin-top: 58px; }
  .news-item.second h3 { margin: 14px 0 6px; }
  .news-item.second p { font-size: 11px; }

  .more-button {
    position: absolute; left: 543px; width: 150px; height: 32px; border-radius: 16px;
    background: var(--pill); box-shadow: inset 0 3px 4px rgba(0,0,0,0.25);
    display: flex; align-items: center; justify-content: center;
    font-size: 12px; color: #222; text-decoration: none;
  }
  .more-button.first { top: 676px; }
  .more-button.second { top: 832px; }

  /* nav */
  .nav-button {
    position: absolute; top: 312px; width: 104px; height: 104px; border-radius: 50%;
    border: 2px solid rgba(255,255,255,0.75);
    box-shadow: 0 2px 5px rgba(0,0,0,0.3);
    display: flex; align-items: center; justify-content: center; text-align: center;
    color: #fff; font-weight: 700; font-size: 17.5px; line-height: 20px; text-decoration: none;
    text-shadow: 1px 2px 2px rgba(0,0,0,0.5); letter-spacing: 0.3px;
  }
  .nav-home { left: 786px; background: radial-gradient(circle at 40% 25%, var(--teal-light), var(--teal-dark)); }
  .nav-contact { left: 911px; background: radial-gradient(circle at 40% 25%, var(--grey-light), var(--grey-dark)); }
  .nav-sites { left: 1036px; background: radial-gradient(circle at 40% 25%, var(--charcoal-light), var(--charcoal-dark)); }

  .aside-copy {
    position: absolute; left: 758px; top: 470px; width: 398px;
    font-size: 14.6px; line-height: 19px; letter-spacing: 0.35px; color: var(--ink-soft);
  }
  .aside-copy p + p { margin-top: 15px; }
  .aside-copy strong { color: var(--ink); }

  .footer-links {
    position: absolute; left: 938px; top: 852px; font-size: 9px; color: var(--muted);
    display: flex; gap: 9px;
  }
  .footer-links a { color: var(--muted); text-decoration: none; }
  .footer-links .sep { color: #bdbdbd; }
</style>
</head>
<body>
<div class="site">
  <div class="aside"></div>
  <div class="aside-halo"></div>
  <div class="currency-badge" aria-hidden="true">$</div>

  <div class="main"></div>
  <div class="main-tab"></div>
  <div class="main-tab-cover"></div>

  <div class="sidebar"></div>
  <div class="sidebar-tab"></div>
  <div class="sidebar-tab-cover"></div>
  <div class="brand-mark">Parallel<br>Press</div>
  <svg class="scroll-arrow" viewBox="0 0 48 56" aria-hidden="true">
    <polygon points="14,0 34,0 34,26 48,26 24,56 0,26 14,26" fill="#c4d8dc"/>
  </svg>
  <div class="section-label">About Us</div>

  <header class="title-pill"><h1>Parallel Press</h1></header>

  <section class="intro">
    <p>Cras neque justo, ultrices at, rhoncus a facilisis eget,nisl. Quisque vitae pede. Nam et augue. Sed a elit. Ut vel massa.Suspendisse ibh pede, ultrices vitae, ultrices nec, mollis non nibh. In sit amet pede quis leo vulputate&nbsp; hendrerit. Cras laoreet leo et justo auctor condim entum. Integer id enim.</p>
    <p>Suspendisse nibh pede, ultrices vitae, ultrices nec, mollis non, nibh. In sit&nbsp; amet pede quis leo vulputate hendrerit.Cras neque justo, ultr-ices at, rhoncus a facilisis eget,nisl. Quisque vitae pede. Nam et augue. Sed a elit.</p>
    <p>Ut vel massa. Suspendisse nibh pede, ultrices vitae, ultrices nec, mollis non nibh. In sit amet pede quis leo vulputate&nbsp; hendrerit. Cras neque justo, ultrices at, rhoncus a facilisis eget,nisl.&nbsp; uisque vitae pede. Nam et augue. Sed a elit. Ut vel massa. Suspendisse nibh pe-de, ultrices vitae, ultrices nec, mollis non nibh. In sit amet pede quis leo vulputate hendrerit.Cras laoreet leo et justo auctor condiment-um. Integer id enim.</p>
  </section>
  <div class="divider"></div>

  <section class="news">
    <h2>Last News</h2>
    <article class="news-item">
      <time>12.06.2011</time>
      <h3>Quisque vitae pede.</h3>
      <p>Suspendisse nibh pede, ultrices vitae, ultrices nec, mollis non, nibh. In sit amet pede quis leo vulputate hendrerit.Cras neque justo, ultrices at, rhoncus a facili-sis eget,nisl. Quisque vitae pede. Nam et augue.</p>
    </article>
    <article class="news-item second">
      <time>12.06.2011</time>
      <h3>Quisque vitae pede.</h3>
      <p>Quisque vitae pede. Nam et augue.Sed a elit. Ut vel massa. Suspen- dissenibh pede, ul-trices vitae,ultrices nec,mollis non nibh...</p>
    </article>
  </section>
  <a class="more-button first" href="#">Learn more...</a>
  <a class="more-button second" href="#">Learn more...</a>

  <nav>
    <a class="nav-button nav-home" href="#">Home<br>Page</a>
    <a class="nav-button nav-contact" href="#">Contact<br>Us</a>
    <a class="nav-button nav-sites" href="#">Our<br>Sites</a>
  </nav>

  <section class="aside-copy">
    <p><strong>Cras neque justo, ultrices at</strong>, rhoncus a facilisis eget,nisl. Quisque vitae pede. Nam et augue. Sed a elit. Ut vel massa.Suspendisse ibh pede,ultrices vitae, ultrices nec, mollis non nibh. In sit amet pe-de quis leo vulputate&nbsp; hendrerit. Cras laoreet leo et justo auctor condimentum. Integer id enim. Su-spendisse nibh pede, ultrices vitae, ultrices nec, mollis non, nibh. In sit&nbsp; amet pede quis leo vulputa-te hendrerit.</p>
    <p><strong>Cras neque justo, ultrices at</strong>, rhoncus a facilisis eget,nisl. Quisque vitae pede. Nam et augue. Sed a elit. Ut vel massa.Suspendisse ibh pede, ultrices vitae, ultrices nec, mollis non nibh. In sit amet pe-de quis leo vulputate&nbsp; hendrerit. Cras laoreet leo et justo auctor condimentum. Integer id enim. Su-spendisse nibh pede.</p>
  </section>

  <footer class="footer-links">
    <a href="#">Contact us</a>
    <a href="#">Terms and Conditions</a>
    <span class="sep">|</span>
    <a href="#">Site map</a>
  </footer>
</div>
</body>
</html>
```